small business focused on life coaching and helping others "create better tomorrows" needs a website

The Pax T Group needs a website that focuses on life coaching and helping others "create better tomorrows"; This is a sole proprietorship so the focus should be on Marla, who has worn many hats and in an excellent position to help others. It should include 6 pages _ Home, Bio, Services, Book, Media, Contact Us and the logo that was created by Lumo Forge; also include testimonials from 5-6 individuals as well as why one might need these services (see file included)

Target Market(s)

Immigrants who need help navigating American system in the workplace, home or community, immigrant or at-risk students unable to communicate with their immigrant parents (due to language or unfamiliarity with the new culture) but would share with someone they trust, those in need of a mentor or help with career advancement or choices, those in need of help with public speaking or leadership development - Marla is someone who has worn many hats and in a position to help - extensive networking, an immigrant herself, former teacher, community leader, TV talk show host, author, mother, grandmother, etc.

Industry/Entity Type

Business

Coding

Coded - Design and coding required

Number of Pages Required

5+ page

Font styles to use
Sans Serif

Colors
cadf82
add136

Requirements
Must have
• visuals of Marla - present image of competency, caring, professionalism; need to include a 30-second video (in process of being produced) of Marla promoting the services, need to include 5-6 testimonials (which will be sent later). Please see the document that describes the different pages of the website and what should be included. Give the image of Marla's ability to help people GROW into a more productive self
Nice to have
• This is a sole proprietor business and as such, need to have people feel comfortable in who I am - trust is critical and that is why experience and competency should be shown

```html
<!DOCTYPE html>
<html lang="en">
<head>
<meta charset="utf-8">
<title>The Pax T Group – Create Better Tomorrows</title>
<link href="https://fonts.googleapis.com/css2?family=Cormorant+Garamond:ital,wght@0,500;0,600;0,700;1,500&family=Lato:ital,wght@0,400;0,700;1,400&display=swap" rel="stylesheet">
<style>
:root{
  --green:#8cc63f;
  --green-light:#add136;
  --green-pale:#cadf82;
  --blue:#4ea2d6;
  --blue-deep:#3a8fc8;
  --teal:#6aa9c4;
  --ink:#555a5f;
  --muted:#7d8287;
  --white:#ffffff;
  --night:#1b1a22;
}
*{box-sizing:border-box;margin:0;padding:0}
html,body{width:1200px;height:2826px;overflow:hidden}
body{position:relative;background:var(--white);font-family:"Lato",Arial,sans-serif;color:var(--ink)}
.abs{position:absolute}
.serif{font-family:"Cormorant Garamond",Georgia,serif}

/* header */
.site-header{top:0;left:0;width:1200px;height:145px;background:var(--white)}
.nav a{position:absolute;top:63px;font-size:18px;color:var(--muted);text-decoration:none}
.nav a.active{color:var(--green)}
.brand{position:absolute;left:480px;top:16px;width:240px;text-align:center}
.brand-dot{width:72px;height:72px;border-radius:50%;border:4px solid var(--green);margin:0 auto 6px}
.brand-name{font-family:"Lato",Arial,sans-serif;font-weight:700;font-size:21px;color:var(--green);white-space:nowrap}

/* hero */
.hero-photo{top:145px;left:0;width:1200px;height:720px;
  background:radial-gradient(ellipse at 55% 55%,#5a4a55 0%,#2b2630 45%,var(--night) 80%),var(--night)}
.hero-title{top:385px;left:0;width:1200px;text-align:center;font-size:60px;font-weight:600;color:var(--white)}
.hero-sub{top:457px;left:0;width:1200px;text-align:center;font-size:22px;color:var(--white)}
.btn-contact{top:505px;left:496px;width:208px;height:46px;border-radius:23px;background:var(--green);
  color:var(--white);font-family:"Cormorant Garamond",Georgia,serif;font-weight:700;font-size:21px;
  letter-spacing:.5px;display:flex;align-items:center;padding-left:22px}
.btn-contact .ring{position:absolute;right:6px;top:5px;width:36px;height:36px;border-radius:50%;border:3px solid var(--white)}
.slide-arrow{top:412px;width:50px;height:50px;border-radius:50%;border:2px solid rgba(255,255,255,.8)}

/* services diagram */
.service-label{font-family:"Cormorant Garamond",Georgia,serif;font-weight:600;font-size:24px;color:var(--white);text-align:center}
.hub{top:729px;left:472px;width:256px;height:256px;border-radius:50%;background:var(--white);
  border:6px solid #e9f3dc;box-shadow:0 0 0 3px var(--green-pale);display:flex;align-items:center;justify-content:center}
.hub-inner{width:206px;height:206px;border-radius:50%;border:5px solid var(--green);display:flex;align-items:center;justify-content:center;text-align:center}
.hub-inner span{font-weight:700;font-size:22px;color:var(--green);line-height:1.2}
.node{width:144px;height:144px;border-radius:50%;background:var(--white);border:5px solid var(--blue);
  display:flex;align-items:center;justify-content:center}

/* nature of business */
.video{top:1475px;left:77px;width:437px;height:292px;background:var(--white);padding:10px}
.video-still{width:100%;height:100%;background:linear-gradient(135deg,#b48e6a 0%,#7e5a48 45%,#3c2f2c 100%);position:relative}
.play{position:absolute;left:50%;top:50%;width:46px;height:46px;margin:-23px 0 0 -23px;border-radius:50%;background:var(--white)}
.nob-title{top:1462px;left:567px;font-size:44px;font-weight:600;color:var(--white)}
.nob-text{top:1524px;left:567px;width:566px;font-size:14px;line-height:24px;color:var(--white)}

/* testimonials */
.section-title{width:1200px;left:0;text-align:center;font-family:"Cormorant Garamond",Georgia,serif;font-weight:700;font-size:44px}
.t-col{width:520px}
.t-head{font-style:italic;font-size:23px;color:var(--ink)}
.t-body{margin-top:10px;font-style:italic;font-size:14.5px;line-height:25px;color:var(--muted)}
.t-name{margin-top:12px;font-size:23px;color:var(--ink)}
.dots{top:2240px;left:560px;width:80px;height:4px}
.dots i{position:absolute;top:0;height:4px;width:34px;background:#cfd3d6}

/* news */
.news-item{top:2425px;width:500px;height:142px}
.news-img{position:absolute;left:0;top:0;width:208px;height:142px}
.news-body{position:absolute;left:232px;top:4px;width:260px;color:var(--white)}
.news-body h3{font-family:"Cormorant Garamond",Georgia,serif;font-weight:700;font-size:20px}
.news-date{font-size:15px;margin:6px 0 4px;display:flex;align-items:center;gap:7px}
.news-body p{font-size:15px;line-height:23px}

/* footer */
.footer-nav a{position:absolute;top:2724px;font-size:16px;color:var(--ink);text-decoration:none}
.copyright{top:2770px;left:77px;font-size:15px;color:var(--ink)}
.social{top:2744px;width:40px;height:40px;border-radius:50%;border:1.5px solid #c3c6c9}
</style>
</head>
<body>

<header class="abs site-header">
  <nav class="nav">
    <a class="active" href="#" style="left:77px">Home</a>
    <a href="#" style="left:158px">Bio</a>
    <a href="#" style="left:232px">Services</a>
    <a href="#" style="left:857px">Book</a>
    <a href="#" style="left:936px">Media</a>
    <a href="#" style="left:1027px">Contact Us</a>
  </nav>
  <div class="brand"><div class="brand-dot"></div><div class="brand-name">The Pax T Group</div></div>
</header>

<div class="abs hero-photo" role="img" aria-label="Photograph of Marla seated on a stage with three guests, flowers behind them"></div>
<h1 class="abs hero-title serif">Create Better Tomorrows.</h1>
<p class="abs hero-sub">Are you an immigrant needing help navigating the American system?</p>
<a class="abs btn-contact">CONTACT US<span class="ring"></span></a>
<div class="abs slide-arrow" style="left:13px"><svg width="46" height="46" viewBox="0 0 46 46"><path d="M23 17l-6 6 6 6M29 17l-6 6 6 6" fill="none" stroke="#fff" stroke-width="2"/></svg></div>
<div class="abs slide-arrow" style="left:1137px"><svg width="46" height="46" viewBox="0 0 46 46"><path d="M17 17l6 6-6 6M23 17l6 6-6 6" fill="none" stroke="#fff" stroke-width="2"/></svg></div>

<svg class="abs" style="top:700px;left:0" width="1200" height="1160" viewBox="0 700 1200 1160">
  <defs>
    <linearGradient id="growGrad" x1="0" y1="0" x2="1" y2="0.35">
      <stop offset="0" stop-color="#8cc63f"/>
      <stop offset="0.5" stop-color="#9cc872"/>
      <stop offset="1" stop-color="#6aa9c4"/>
    </linearGradient>
  </defs>
  <path d="M0,722 Q600,882 1200,722 L1200,1420 L0,1420Z" fill="url(#growGrad)"/>
  <path d="M0,1290 Q200,1240 380,1280 T760,1270 T1200,1250 L1200,1420 L0,1420Z" fill="#ffffff" opacity=".12"/>
  <path d="M0,1404 Q600,1252 1200,1404 L1200,1860 L0,1860Z" fill="#4ea2d6"/>
  <g stroke="#ffffff" stroke-width="5">
    <line x1="600" y1="857" x2="324" y2="910"/>
    <line x1="600" y1="857" x2="437" y2="1051"/>
    <line x1="600" y1="857" x2="600" y2="1140"/>
    <line x1="600" y1="857" x2="754" y2="1036"/>
    <line x1="600" y1="857" x2="878" y2="910"/>
  </g>
</svg>

<div class="abs hub"><div class="hub-inner"><span>The Pax T<br>Group</span></div></div>

<div class="abs node" style="left:252px;top:838px"><svg width="60" height="60" viewBox="0 0 60 60" fill="#4ea2d6"><circle cx="30" cy="12" r="6"/><rect x="24" y="20" width="12" height="12" rx="3"/><rect x="14" y="30" width="32" height="6"/><path d="M19 36h22l-3 18H22z"/></svg></div>
<div class="abs node" style="left:365px;top:979px"><svg width="60" height="60" viewBox="0 0 60 60"><rect x="8" y="18" width="44" height="32" rx="4" fill="#4ea2d6"/><rect x="22" y="10" width="16" height="10" rx="2" fill="none" stroke="#4ea2d6" stroke-width="3"/><rect x="8" y="31" width="44" height="3" fill="#fff"/></svg></div>
<div class="abs node" style="left:528px;top:1068px"><svg width="64" height="60" viewBox="0 0 64 60" fill="none" stroke="#4ea2d6" stroke-width="4"><circle cx="32" cy="30" r="24"/><path d="M14 28h12l6-5 8 5h10M20 34h24" stroke-linecap="round"/></svg></div>
<div class="abs node" style="left:682px;top:964px"><svg width="60" height="60" viewBox="0 0 60 60" fill="#4ea2d6"><rect x="8" y="36" width="8" height="14"/><rect x="20" y="28" width="8" height="22"/><circle cx="40" cy="12" r="5"/><rect x="35" y="19" width="10" height="31"/><rect x="6" y="50" width="48" height="3"/></svg></div>
<div class="abs node" style="left:806px;top:838px"><svg width="60" height="60" viewBox="0 0 60 60" fill="#4ea2d6"><circle cx="14" cy="14" r="5"/><rect x="9" y="21" width="10" height="30"/><rect x="24" y="8" width="30" height="24" fill="none" stroke="#4ea2d6" stroke-width="3"/><rect x="29" y="22" width="4" height="7"/><rect x="36" y="17" width="4" height="12"/><rect x="43" y="13" width="4" height="16"/><rect x="37" y="32" width="3" height="18"/></svg></div>

<div class="abs service-label" style="left:60px;top:915px;width:210px">public speaking</div>
<div class="abs service-label" style="left:230px;top:1063px;width:150px">Careers</div>
<div class="abs service-label" style="left:480px;top:1232px;width:240px">inter-generational<br>relations</div>
<div class="abs service-label" style="left:840px;top:1063px;width:250px">leadership development</div>
<div class="abs service-label" style="left:955px;top:915px;width:160px">acculturation</div>

<div class="abs video"><div class="video-still" role="img" aria-label="Video still of Marla speaking at a microphone"><span class="play"><svg width="46" height="46" viewBox="0 0 46 46"><path d="M18 14l14 9-14 9z" fill="#6b5a52"/></svg></span></div></div>
<h2 class="abs nob-title serif">Nature of Business</h2>
<p class="abs nob-text">Life coach (this is a business that is focused on the individual – Marla Venn.&nbsp; As such, need to present Marla as a mature professional with extensive experience in working with people and someone who has been very effective in getting things done.&nbsp; Aside from her personal experience as an immigrant, parent and grandparent, Marla has decades of experience as a teacher and administrator in a number of school systems, Director of a countywide agency, community leader heading a national organization with chapters nationally, talk show host, public speaker/facilitator/emcee, human resource administrator responsive for recruitment and compliance issues, board member for numerous commissions and organizations, etc.</p>

<h2 class="abs section-title" style="top:1896px;color:var(--green)">Testimonials</h2>
<div class="abs t-col" style="left:77px;top:1985px">
  <p class="t-head">"Immigrant with acculturation issues"</p>
  <p class="t-body">Marla is my "Go-To Person For Just About Anything. She Has Been a Significant support in My Acculturation Into Western/Western Culture - Helping Me Navigate the Many aspects Of Life's Journey.Through Her Guidance, I Have Gained Much Confidence in Myself and in my approach to Resolving Issues.</p>
  <p class="t-name">- Rena P</p>
</div>
<div class="abs t-col" style="left:625px;top:1985px">
  <p class="t-head">"Support for career"</p>
  <p class="t-body">Marla is my "Go-To Person For Just About Anything. She Has Been a Significant support in My Acculturation Into Western/Western Culture - Helping Me Navigate the Many aspects Of Life's Journey.Through Her Guidance, I Have Gained Much Confidence in Myself and in my approach to Resolving Issues.</p>
  <p class="t-name">- Tavi D</p>
</div>
<div class="abs dots"><i style="left:0;background:var(--blue)"></i><i style="left:42px"></i></div>

<svg class="abs" style="top:2289px;left:0" width="1200" height="400" viewBox="0 2289 1200 400">
  <defs>
    <linearGradient id="newsGrad" x1="0" y1="0" x2="1" y2="0">
      <stop offset="0" stop-color="#8cc63f"/>
      <stop offset="1" stop-color="#4ea2d6"/>
    </linearGradient>
  </defs>
  <path d="M0,2289 L1200,2289 L1200,2592 Q600,2762 0,2592Z" fill="url(#newsGrad)"/>
</svg>
<h2 class="abs section-title" style="top:2340px;color:var(--white)">Latest News</h2>
<article class="abs news-item" style="left:81px">
  <div class="news-img" role="img" aria-label="Photo of Marla with a guest at an event" style="background:linear-gradient(135deg,#d9c3a8,#8c6d5a)"></div>
  <div class="news-body">
    <h3>Lorem Ipsum is simply dummy</h3>
    <div class="news-date"><svg width="14" height="14" viewBox="0 0 14 14" fill="#fff"><rect x="1" y="3" width="12" height="10" rx="1"/><rect x="3" y="1" width="2" height="3"/><rect x="9" y="1" width="2" height="3"/></svg>April 06, 2017</div>
    <p>Lorem ipsum dolor sit amet, consectetur adipiscing elit. Etiam fringilla odio in mollis tincidunt</p>
  </div>
</article>
<article class="abs news-item" style="left:629px">
  <div class="news-img" role="img" aria-label="Photo of Marla with a guest at an interview" style="background:linear-gradient(135deg,#c9b9a6,#5e5249)"></div>
  <div class="news-body">
    <h3>Lorem Ipsum is simply dummy</h3>
    <div class="news-date"><svg width="14" height="14" viewBox="0 0 14 14" fill="#fff"><rect x="1" y="3" width="12" height="10" rx="1"/><rect x="3" y="1" width="2" height="3"/><rect x="9" y="1" width="2" height="3"/></svg>April 06, 2017</div>
    <p>Lorem ipsum dolor sit amet, consectetur adipiscing elit. Etiam fringilla odio in mollis tincidunt</p>
  </div>
</article>

<footer>
  <nav class="footer-nav">
    <a href="#" style="left:77px">Home</a>
    <a href="#" style="left:148px">Bio</a>
    <a href="#" style="left:200px">Services</a>
    <a href="#" style="left:284px">Book</a>
    <a href="#" style="left:343px">Media</a>
    <a href="#" style="left:423px">Contact Us</a>
  </nav>
  <p class="abs copyright">©<b>THE PAX T GROUP</b>- 2017. All Rights Reserved.</p>
  <a class="abs social" style="left:981px" aria-label="Social profile"></a>
  <a class="abs social" style="left:1033px" aria-label="Social profile"></a>
  <a class="abs social" style="left:1084px" aria-label="Social profile"></a>
</footer>

</body>
</html>
```